RWM Bricklaying business card

i need a business card designed for my bricklaying company.
I was also hoping to get a logo drawn up so i can put it on some t-shirts.
You can use any style or colours just as long as it lloks good. thanks Dallas

Dallas Whitby
RWM Bricklaying
0471395067
Any type of brick/blockwork
No job too small

```html
<!DOCTYPE html>
<html lang="en">
<head>
<meta charset="utf-8">
<title>RWM Bricklaying – Business Card</title>
<link rel="stylesheet" href="https://fonts.googleapis.com/css2?family=Open+Sans:wght@400;600;800&display=swap">
<style>
  :root {
    --backdrop: #e9e4df;
    --card-white: #f3f3f2;
    --brick-orange: #c9502f;
    --ink-dark: #1f1f1f;
    --text-light: #ffffff;
    --worker-blue: #3f6fb5;
    --shadow: rgba(0, 0, 0, 0.18);
  }
  * { box-sizing: border-box; margin: 0; padding: 0; }
  html, body {
    width: 1200px;
    height: 675px;
    overflow: hidden;
    background: var(--backdrop);
    font-family: "Open Sans", Arial, sans-serif;
  }
  .business-card {
    position: absolute;
    left: 180px;
    top: 97px;
    width: 840px;
    height: 480px;
    display: flex;
    background: var(--card-white);
    box-shadow: 0 10px 30px var(--shadow);
  }
  .brand-side {
    width: 45%;
    display: flex;
    flex-direction: column;
    align-items: center;
    justify-content: center;
    gap: 22px;
    padding: 30px;
  }
  .mascot-illustration {
    width: 250px;
    height: 200px;
    border-radius: 6px;
    background: linear-gradient(180deg, var(--worker-blue) 0%, #8aa6d1 45%, var(--brick-orange) 100%);
  }
  .brand-name {
    font-weight: 800;
    font-size: 34px;
    letter-spacing: 1px;
    text-transform: uppercase;
    color: var(--ink-dark);
    text-align: center;
    line-height: 1.15;
  }
  .info-side {
    position: relative;
    width: 55%;
    background: var(--brick-orange);
    color: var(--text-light);
    padding: 72px 40px 0 48px;
  }
  .tab {
    position: absolute;
    left: 0;
    width: 14px;
    height: 16px;
    background: var(--card-white);
  }
  .tab--name { top: 86px; }
  .tab--phone { top: 128px; }
  .tab--service { top: 298px; }
  .tab--promise { top: 326px; }
  .contact-name {
    font-size: 30px;
    font-weight: 600;
    line-height: 1.2;
  }
  .contact-phone {
    display: flex;
    align-items: center;
    gap: 8px;
    margin-top: 8px;
    font-size: 19px;
  }
  .contact-phone svg { width: 16px; height: 16px; fill: var(--text-light); }
  .services {
    list-style: none;
    margin-top: 138px;
    font-size: 21px;
    line-height: 1.35;
  }
</style>
</head>
<body>
  <article class="business-card">
    <section class="brand-side">
      <div class="mascot-illustration" role="img" aria-label="Cartoon bricklayer in a blue cap laying bricks on a wall"></div>
      <div class="brand-name">RWM Bricklaying</div>
    </section>
    <section class="info-side">
      <span class="tab tab--name"></span>
      <span class="tab tab--phone"></span>
      <span class="tab tab--service"></span>
      <span class="tab tab--promise"></span>
      <h1 class="contact-name">Dallas Whitby</h1>
      <p class="contact-phone">
        <svg viewBox="0 0 24 24" aria-hidden="true"><path d="M6.6 10.8a15.1 15.1 0 0 0 6.6 6.6l2.2-2.2c.3-.3.7-.4 1-.2 1.1.4 2.3.6 3.6.6.6 0 1 .4 1 1V20c0 .6-.4 1-1 1C10.6 21 3 13.4 3 4c0-.6.4-1 1-1h3.5c.6 0 1 .4 1 1 0 1.3.2 2.5.6 3.6.1.3 0 .7-.2 1z"/></svg>
        0471395067
      </p>
      <ul class="services">
        <li>Any type of brick/blockwork</li>
        <li>No job too small</li>
      </ul>
    </section>
  </article>
</body>
</html>
```